Independent Financial Advisor Billboard Campaign - Granite Bridge Financial

I am a local, independent financial advisor. My company is Granite Bridge Financial, located in Charleston, WV. My main source of revenue comes from those nearing or entering retirement that need assistance with financial planning and investment management. Many are looking to rollover their employer retirement plan into an IRA account. I would like a billboard design campaign that focuses on this type of client. Please see our website www.granitebridgefinancial-example.com for more information.

```html
<!DOCTYPE html>
<html lang="en">
<head>
<meta charset="utf-8">
<title>Granite Bridge Financial – Retirement Billboard</title>
<link rel="stylesheet" href="https://fonts.googleapis.com/css2?family=Oswald:wght@500;600;700&family=Roboto+Condensed:wght@700&display=swap">
<style>
  :root {
    --backdrop: #3b3b3b;
    --sky-blue: #45a5da;
    --navy: #184679;
    --ink: #050505;
    --paper: #ffffff;
    --stone: #b5b5b6;
    --suit-dark: #243a6a;
    --suit-light: #eef0f4;
    --skin: #d9bfae;
  }
  * { margin: 0; padding: 0; box-sizing: border-box; }
  html, body {
    width: 1200px;
    height: 1200px;
    overflow: hidden;
    background: var(--backdrop);
  }
  .billboard {
    position: absolute;
    left: 40px;
    top: 320px;
    width: 1120px;
    height: 559px;
    display: block;
  }
  .service-label {
    font-family: 'Oswald', sans-serif;
    font-weight: 600;
    font-size: 46px;
    fill: var(--navy);
  }
  .headline {
    font-family: 'Oswald', sans-serif;
    font-weight: 600;
    font-size: 172px;
  }
  .headline--top { fill: var(--ink); }
  .headline--bottom { fill: var(--navy); }
  .phone-number {
    font-family: 'Oswald', sans-serif;
    font-weight: 700;
    font-size: 70px;
    fill: var(--paper);
  }
  .web-address {
    font-family: 'Roboto Condensed', sans-serif;
    font-weight: 700;
    font-size: 25px;
    fill: var(--paper);
  }
  .brand-name {
    font-family: 'Oswald', sans-serif;
    font-weight: 500;
    font-size: 40px;
    fill: var(--navy);
  }
</style>
</head>
<body>
<svg class="billboard" viewBox="0 0 1120 559" xmlns="http://www.w3.org/2000/svg">
  <defs>
    <linearGradient id="portrait-tone" x1="0" y1="0" x2="0" y2="1">
      <stop offset="0" stop-color="var(--suit-light)"/>
      <stop offset="0.3" stop-color="var(--skin)"/>
      <stop offset="0.55" stop-color="#9aa4bb"/>
      <stop offset="0.75" stop-color="var(--suit-dark)"/>
      <stop offset="1" stop-color="var(--suit-dark)"/>
    </linearGradient>
  </defs>

  <rect class="board-surface" x="0" y="0" width="1120" height="559" fill="var(--paper)"/>

  <!-- services band -->
  <g class="services-band">
    <path d="M0 0 H1120 V87 H765 Q782 80 789 0 H436 Q430 80 390 87 H0 Z" fill="var(--sky-blue)"/>
    <path d="M0 87 H390 Q430 80 436 0 H789 Q782 80 765 87" fill="none"/>
    <path d="M436 0 Q430 80 390 87" fill="none" stroke="var(--paper)" stroke-width="3"/>
    <path d="M789 0 Q782 80 765 87" fill="none" stroke="var(--paper)" stroke-width="3"/>
    <text class="service-label" x="30" y="66" textLength="370" lengthAdjust="spacingAndGlyphs">RETIREMENT PLANNING</text>
    <text class="service-label" x="448" y="66" textLength="300" lengthAdjust="spacingAndGlyphs">COLLEGE PLANNING</text>
    <text class="service-label" x="806" y="66" textLength="287" lengthAdjust="spacingAndGlyphs">ESTATE PLANNING</text>
  </g>

  <!-- advisor portrait area -->
  <rect class="advisor-portrait" x="760" y="87" width="360" height="362" fill="url(#portrait-tone)"
        role="img" aria-label="Portrait photo of the advisor in a navy suit and patterned tie"/>

  <!-- headline -->
  <text class="headline headline--top" x="45" y="266" textLength="699" lengthAdjust="spacingAndGlyphs">RETIREMENT</text>
  <text class="headline headline--bottom" x="39" y="406" textLength="710" lengthAdjust="spacingAndGlyphs">DONE RIGHT.</text>

  <!-- contact band -->
  <g class="contact-band">
    <path d="M0 447 H625 Q605 455 594 480 L551 559 H0 Z" fill="var(--navy)"/>
    <path d="M654 449 H1120 V559 H563 L606 480 Q620 452 654 449 Z" fill="var(--stone)"/>
    <g class="phone-icon">
      <path d="M36 468 L46 464 L53 480 L47 485 Q51 496 60 504 L66 499 L79 508 L75 517 Q70 522 60 518 Q40 506 32 484 Q30 474 36 468 Z" fill="var(--paper)"/>
      <path d="M58 478 Q66 482 68 490" fill="none" stroke="var(--paper)" stroke-width="3" stroke-linecap="round"/>
      <path d="M60 467 Q75 472 79 488" fill="none" stroke="var(--paper)" stroke-width="3" stroke-linecap="round"/>
    </g>
    <text class="phone-number" x="88" y="514" textLength="448" lengthAdjust="spacingAndGlyphs">304.555.0142</text>
    <text class="web-address" x="34" y="550" textLength="488" lengthAdjust="spacingAndGlyphs">www.granitebridgefinancial-example.com</text>
  </g>

  <!-- brand lockup -->
  <g class="brand-lockup">
    <rect x="664" y="472" width="60" height="60" fill="var(--navy)"/>
    <text class="brand-name" x="748" y="522" textLength="320" lengthAdjust="spacingAndGlyphs">GRANITE BRIDGE</text>
  </g>
</svg>
</body>
</html>
```